Vellmar Detailing – Premium Automotive Detailing Studio Website Design

We're launching a premium automotive detailing studio called Vellmar Detailing, and we’re looking for a clean, minimal, and high-end website design (desktop + mobile version). The studio targets owners of luxury vehicles who care deeply about aesthetics, perfection, and exceptional service.
This project is about more than just showing services , it should feel like a luxury experience from the very first second. The design should be modern, minimalistic, elegant, and clearly aimed at an upscale market.
We’re looking for a designer who can translate our physical studio’s premium interior and architectural feel into a digital presence.
What we want the website to feel like:
Clean and modern
Professional and luxurious
Minimal and not cluttered
Light animations or transitions to add polish
Stylish and cinematic
Design freedom:
We trust your design direction. We are not providing strict color codes or layout instructions, we want you to create what you believe works best based on our brand positioning and target audience. Just keep it premium, modern, and well-organized.
What the website should include:
Hero section with a bold visual (image or video)
About the Studio — a few blocks explaining our story and focus on quality
Service Overview — clearly showing what we offer (detailing, ceramic coating, interior, etc.)
Gallery/Showcase — show off our work with cars, interior, and the space itself
Client Lounge Area — mention comfort, coffee, and waiting space
Testimonials — social proof from satisfied clients
Location & contact section — map, address, contact form
Footer, simple with nav, contact info, and optional social media
Target audience:
Owners of high-end vehicles (Torvani, Kellard, etc.)
Car collectors and detailing enthusiasts
People looking for premium-level service and presentation
Brands/creators booking our photo studio

```html
<!DOCTYPE html>
<html lang="en">
<head>
<meta charset="utf-8">
<title>Vellmar Detailing – Premium Automotive Detailing</title>
<link href="https://fonts.googleapis.com/css2?family=Saira:wght@500;600;700&family=Poppins:wght@400;500;600&display=swap" rel="stylesheet">
<style>
  :root{
    --ink:#0b0b0c;
    --black:#000;
    --white:#fff;
    --paper:#ffffff;
    --mist:#e9e9eb;
    --grey-btn:#2b2b2d;
    --text:#1c1c1e;
    --muted:#8a8a8e;
    --line:#d2d2d6;
    --head:'Saira', sans-serif;
    --body:'Poppins', sans-serif;
  }
  *{margin:0;padding:0;box-sizing:border-box}
  html,body{width:1200px;height:5106px;overflow:hidden;background:var(--paper)}
  body{position:relative;font-family:var(--body);color:var(--text)}
  .abs{position:absolute}
  .photo{position:absolute}

  /* Hero */
  .hero{position:absolute;left:0;top:0;width:1200px;height:760px}
  .hero-bg{position:absolute;left:0;top:0;width:1200px;height:705px;background:var(--black)}
  .hero-photo{position:absolute;left:0;top:0;width:1200px;height:755px;
    background:linear-gradient(160deg,#1c1c1e 0%,#3f4145 30%,#8d9095 52%,#55585c 70%,#2a2b2d 100%);
    clip-path:polygon(620px 0,1200px 0,1200px 755px,500px 755px)}
  .menu-btn{left:45px;top:25px;width:40px;height:40px;background:#2e2e30;display:flex;align-items:center;justify-content:center}
  .brand-top{left:0;width:1200px;top:30px;text-align:center;color:var(--white);font-family:var(--head);font-weight:600;font-size:17px;letter-spacing:2px;line-height:17px}
  .brand-top small{display:block;font-size:10px;letter-spacing:5px}
  .lang{left:1048px;top:34px;color:var(--white);font-size:14px;display:flex;gap:6px;align-items:center}
  .hero h1{left:88px;top:230px;color:var(--white);font-family:var(--head);font-weight:700;font-size:56px;line-height:62px}
  .hero .sub{left:88px;top:374px;color:var(--white);font-family:var(--head);font-weight:600;font-size:19px;line-height:25px}
  .btn{display:flex;align-items:center;justify-content:center;font-family:var(--head);font-weight:600;font-size:14px;color:var(--white)}
  .hero .btn{left:88px;top:447px;width:230px;height:46px;background:var(--grey-btn)}
  .counter{left:405px;top:622px;color:var(--white);font-family:var(--head);font-weight:700;font-size:32px}
  .counter span{font-size:16px}

  /* About */
  .lead-line{height:2px;background:var(--ink)}
  .lead-line::after{content:"";position:absolute;right:-2px;top:-3px;width:8px;height:8px;border-radius:50%;background:var(--ink)}
  .about h2{left:132px;top:866px;font-family:var(--head);font-weight:600;font-size:38px;line-height:46px}
  .about p{left:495px;top:860px;width:590px;font-size:14px;line-height:27px}
  .about-band{left:0;top:1010px;width:1200px;height:365px;background:linear-gradient(180deg,#f3f3f6,#ebebef);clip-path:polygon(0 12px,1200px 0,1200px 365px,0 365px)}
  .car-about{left:178px;top:1035px;width:660px;height:250px;border-radius:120px 140px 30px 30px;
    background:linear-gradient(180deg,#2a2b2e 0%,#5b5d61 22%,#f4f4f6 40%,#e4e5e8 70%,#3c3d40 100%)}
  .car-about-2{left:790px;top:1092px;width:236px;height:110px;border-radius:60px 70px 18px 18px;
    background:linear-gradient(180deg,#3a3b3e 0%,#f3f3f5 35%,#e5e5e8 70%,#4a4b4e 100%)}

  /* Services */
  .services-bg{left:0;top:1375px;width:1200px;height:670px;background:var(--mist)}
  .services h2{left:120px;top:1462px;font-family:var(--head);font-weight:700;font-size:52px}
  .svc-active{left:120px;top:1634px;font-family:var(--head);font-weight:600;font-size:25px}
  .svc-desc{left:122px;top:1682px;font-size:14px;line-height:26px;font-weight:500}
  .svc-rule{left:120px;top:1755px;width:310px;height:1px;background:#9c9ca0}
  .svc-item{left:120px;font-family:var(--head);font-weight:600;font-size:16px}
  .car-svc{left:400px;top:1605px;width:800px;height:520px;border-radius:160px 0 40px 40px;
    background:linear-gradient(180deg,#1e1f21 0%,#4a4c50 22%,#f6f6f7 34%,#e8e8ea 58%,#bfc0c3 72%,#2a2b2d 88%,#e9e9eb 100%)}

  /* Gallery */
  .gallery h2{left:705px;top:2742px;font-family:var(--head);font-weight:600;font-size:35px}
  .gallery p{left:705px;top:2805px;width:385px;font-size:14px;line-height:27px;font-weight:500}

  /* Lounge */
  .lounge h2{left:83px;top:3710px;color:var(--white);font-family:var(--head);font-weight:700;font-size:35px}
  .lounge p{left:83px;top:3770px;width:720px;color:var(--white);font-size:14px;line-height:27px;font-weight:500}

  /* Testimonials */
  .quote-mark{left:175px;top:3900px;font-family:var(--head);font-weight:700;font-size:520px;line-height:520px;background:linear-gradient(180deg,#d8d8da 10%,#ffffff 45%);-webkit-background-clip:text;background-clip:text;color:transparent}
  .testi h2{left:525px;top:4018px;font-family:var(--head);font-weight:600;font-size:35px}
  .testi p{left:525px;top:4078px;width:470px;font-size:14px;line-height:26px}
  .testi .who{left:525px;top:4140px;font-size:15px;font-weight:600}
  .divider{left:82px;top:4255px;width:1036px;height:1px;background:var(--line)}

  /* Contact */
  .contact h2{left:215px;top:4388px;font-family:var(--head);font-weight:600;font-size:33px}
  .field{border-bottom:1px solid var(--line);font-size:12px;color:var(--muted);padding:0 0 10px 12px;font-weight:500}
  .contact .btn{left:215px;top:4640px;width:157px;height:42px;background:var(--ink)}

  /* Footer */
  .footer{left:0;top:4828px;width:1200px;height:278px;background:var(--black)}
  .footer-brand{left:92px;top:4920px;color:var(--white);font-family:var(--head);font-weight:600;font-size:38px;line-height:36px;letter-spacing:2px;display:flex;gap:16px;align-items:center}
  .footer-brand small{display:block;font-size:22px;letter-spacing:12px;line-height:26px}
  .footer-brand .mark{width:52px;height:52px;border:3px solid var(--white)}
  .socials{left:520px;top:4942px;display:flex;gap:10px}
  .socials span{width:32px;height:32px;background:#1f1f21}
  .foot-nav{left:760px;top:4950px;display:flex;gap:28px;color:var(--white);font-size:13px}
  .to-top{left:1150px;top:5005px;width:32px;height:32px;background:#1f1f21;display:flex;align-items:center;justify-content:center}
  .copy{left:0;width:1200px;top:5066px;text-align:center;color:#bdbdc0;font-size:12px}
</style>
</head>
<body>

<header class="hero">
  <div class="hero-bg"></div>
  <div class="hero-photo" role="img" aria-label="Dark silver luxury sports car driving at dusk"></div>
  <div class="abs menu-btn"><svg width="14" height="12" viewBox="0 0 14 12"><path d="M0 1h14M0 6h14M0 11h14" stroke="#fff" stroke-width="1.5"/></svg></div>
  <div class="abs brand-top">VELLMAR<small>DETAILING</small></div>
  <div class="abs lang"><svg width="14" height="14" viewBox="0 0 14 14"><circle cx="7" cy="7" r="6" fill="none" stroke="#fff" stroke-width="1.4"/><path d="M1 7h12M7 1c-3 3-3 9 0 12M7 1c3 3 3 9 0 12" stroke="#fff" stroke-width="1" fill="none"/></svg>Eng ▾</div>
  <h1 class="abs">Where Luxury<br>Meets Precision</h1>
  <div class="abs sub">Premium Automotive Detailing for the<br>Discerning Car Owner</div>
  <div class="abs btn">Book Your Appointment</div>
  <div class="abs counter">01 <span>/ 04</span></div>
</header>

<section class="about">
  <div class="abs lead-line" style="left:45px;top:891px;width:65px"></div>
  <h2 class="abs">A Studio Built<br>for Excellence</h2>
  <p class="abs">At Vellmar Detailing, we believe detailing is an art — not just a service. Our studio was created for those who value craftsmanship, aesthetics, and flawless execution. From our advanced techniques to our elegant space, every detail reflects our commitment to perfection.</p>
  <div class="abs about-band"></div>
  <div class="photo car-about" role="img" aria-label="White supercar in front three-quarter view"></div>
  <div class="photo car-about-2" role="img" aria-label="Second white supercar in the background"></div>
</section>

<section class="services">
  <div class="abs services-bg"></div>
  <div class="abs lead-line" style="left:35px;top:1495px;width:65px"></div>
  <h2 class="abs">Our Signature Services</h2>
  <svg class="abs" style="left:975px;top:1482px" width="105" height="30" viewBox="0 0 105 30"><path d="M32 15H2M12 6 2 15l10 9" stroke="#333" stroke-width="2" fill="none"/><path d="M58 15h44M92 5l10 10-10 10" stroke="#111" stroke-width="2.6" fill="none"/></svg>
  <div class="abs lead-line" style="left:75px;top:1652px;width:38px"></div>
  <div class="abs svc-active">Exterior Detailing</div>
  <div class="abs svc-desc">Restore your vehicle's brilliance with<br>paint-safe, high-gloss polishing.</div>
  <div class="abs svc-rule"></div>
  <div class="abs svc-item" style="top:1780px;color:#6e6e72">Interior Detailing</div>
  <div class="abs svc-item" style="top:1822px;color:#8a8a8e">Ceramic Coating</div>
  <div class="abs svc-item" style="top:1864px;color:#a9a9ad">Paint Correction</div>
  <div class="abs svc-item" style="top:1903px;color:#c6c6ca">Maintenance Packages</div>
  <div class="photo car-svc" role="img" aria-label="White luxury saloon seen from the front"></div>
</section>

<section class="gallery">
  <div class="photo" style="left:238px;top:2283px;width:230px;height:129px;background:linear-gradient(180deg,#e9eaec 0%,#f7f7f8 45%,#c9cacd 70%,#55565a 100%)" role="img" aria-label="White grand tourer in profile"></div>
  <div class="photo" style="left:506px;top:2232px;width:319px;height:180px;background:linear-gradient(180deg,#6a6b6f 0%,#2a2b2e 40%,#131314 75%,#5b5c60 100%)" role="img" aria-label="Black performance estate car"></div>
  <div class="photo" style="left:864px;top:2307px;width:166px;height:318px;background:linear-gradient(180deg,#e4ecf1 0%,#9fae8e 38%,#d7d3cd 60%,#4f4e4d 100%)" role="img" aria-label="Silver coupe under palm trees"></div>
  <div class="photo" style="left:158px;top:2446px;width:482px;height:376px;background:linear-gradient(180deg,#dcdde0 0%,#f5f5f6 35%,#ffffff 55%,#b5b7ba 80%,#6b6c70 100%)" role="img" aria-label="White hypercar with doors open in a bright studio"></div>
  <div class="photo" style="left:640px;top:2446px;width:185px;height:222px;background:linear-gradient(180deg,#d9dadd 0%,#f4f4f5 50%,#c3c4c7 100%)" role="img" aria-label="Studio wall and raised door"></div>
  <div class="photo" style="left:162px;top:2857px;width:230px;height:128px;background:linear-gradient(180deg,#b9bbbf 0%,#e6e7e9 45%,#8a8c90 75%,#4c4d50 100%)" role="img" aria-label="Silver sports car outdoors"></div>
  <div class="photo" style="left:431px;top:2857px;width:209px;height:313px;background:linear-gradient(180deg,#a4a5a8 0%,#eeeef0 35%,#dcdde0 65%,#8d8f92 100%)" role="img" aria-label="Close-up of a white hypercar front wheel"></div>
  <h2 class="abs">Our Craft in Motion</h2>
  <p class="abs">Explore our portfolio of luxury vehicles, client favorites, and behind-the-scenes shots from our detailing studio. Precision, beauty, and dedication — all on display.</p>
  <svg class="abs" style="left:705px;top:2945px" width="90" height="26" viewBox="0 0 90 26"><path d="M28 13H2M10 6 2 13l8 7" stroke="#333" stroke-width="2" fill="none"/><path d="M48 13h38M78 5l8 8-8 8" stroke="#111" stroke-width="2.4" fill="none"/></svg>
</section>

<section class="lounge">
  <div class="photo" style="left:0;top:3290px;width:1200px;height:610px;background:linear-gradient(180deg,#3e3a35 0%,#c9ccc4 25%,#b7b9b4 55%,#5e5b57 80%,#4a4743 100%)" role="img" aria-label="Client lounge with leather armchair, curved sofa and large windows"></div>
  <h2 class="abs">Relax While We Perfect Your Vehicle</h2>
  <p class="abs">Our private client lounge is designed for your comfort. Enjoy freshly brewed coffee, fast Wi-Fi, and a quiet, stylish space while your car receives our full attention.</p>
</section>

<section class="testi">
  <div class="abs quote-mark">“</div>
  <h2 class="abs">What Our Clients Say</h2>
  <p class="abs">“Vellmar Detailing is in a league of its own. My Kellard has never looked this good.”</p>
  <div class="abs who">— Lukas M.</div>
  <div class="abs divider"></div>
</section>

<section class="contact">
  <h2 class="abs">Get in Touch</h2>
  <div class="abs field" style="left:215px;top:4468px;width:157px">Your Name</div>
  <div class="abs field" style="left:388px;top:4468px;width:157px">Email Address</div>
  <div class="abs field" style="left:215px;top:4521px;width:157px">Phone number</div>
  <div class="abs field" style="left:388px;top:4521px;width:157px">Vehicle Type</div>
  <div class="abs field" style="left:215px;top:4575px;width:330px">Message</div>
  <div class="abs btn">Send Inquiry</div>
  <div class="photo" style="left:615px;top:4360px;width:368px;height:368px;background:linear-gradient(135deg,#e2e2e3,#cfcfd1 50%,#dcdcdd)" role="img" aria-label="City map showing the studio location"></div>
  <svg class="abs" style="left:800px;top:4482px" width="34" height="60" viewBox="0 0 34 60"><circle cx="17" cy="17" r="14" fill="#d01f1f"/><path d="M17 31v28" stroke="#777" stroke-width="2"/></svg>
</section>

<footer>
  <div class="abs footer"></div>
  <div class="abs footer-brand"><span class="mark"></span><div>VELLMAR<small>DETAILING</small></div></div>
  <div class="abs socials"><span></span><span></span><span></span><span></span></div>
  <nav class="abs foot-nav"><span>Home</span><span>About</span><span>Services</span><span>Gallery</span><span>Contact</span></nav>
  <div class="abs to-top"><svg width="10" height="12" viewBox="0 0 10 12"><path d="M5 12V1M1 5l4-4 4 4" stroke="#fff" stroke-width="1.4" fill="none"/></svg></div>
  <div class="abs copy">© Copyright 2025 Vellmar Detailing. All rights reserved.</div>
</footer>

</body>
</html>
```